New Webpage for High Class Expert Witness Services Company

We are looking for a minimalist design for a webpage that just has our logo and an entry form offer to connect with one of our Liaisons.
The entry form should just ask for Name, Email, Contact Info and Description of Project.

Company Name is: The Marlow Crest Advisory Services

Number of Pages Required

1 page

```html
<!DOCTYPE html>
<html lang="en">
<head>
<meta charset="utf-8">
<title>The Marlow Crest Advisory Services — Connect with a Liaison</title>
<link href="https://fonts.googleapis.com/css2?family=Figtree:wght@300;400;600&display=swap" rel="stylesheet">
<style>
  :root {
    --bg-deep: #050505;
    --bg-soft: #1a1a1a;
    --card-edge: #3b3b3b;
    --text: #f2f2f2;
    --muted: #c9c9c9;
    --field: #dcdcdc;
    --gold-top: #d7aa5c;
    --gold-bottom: #7b6031;
  }
  * { box-sizing: border-box; margin: 0; padding: 0; }
  html, body { width: 1200px; height: 675px; overflow: hidden; }
  body {
    position: relative;
    font-family: "Figtree", sans-serif;
    color: var(--text);
    background: radial-gradient(ellipse 70% 80% at 85% 55%, var(--bg-soft), var(--bg-deep) 70%);
  }
  .brand {
    position: absolute;
    left: 0; top: 84px; width: 1200px;
    text-align: center;
    color: var(--muted);
    font-weight: 400;
  }
  .brand-name {
    font-size: 17px;
    letter-spacing: 1.6px;
    line-height: 24px;
  }
  .brand-tagline {
    margin-top: 8px;
    font-size: 8px;
    letter-spacing: 2.2px;
  }
  .liaison-card {
    position: absolute;
    left: 425px; top: 163px;
    width: 352px; height: 411px;
    border-radius: 28px;
    border: 1px solid var(--card-edge);
    background: linear-gradient(160deg, #191919, #222222);
  }
  .card-title {
    position: absolute;
    left: 0; top: 22px; width: 100%;
    text-align: center;
    font-size: 23px;
    font-weight: 300;
    letter-spacing: -0.2px;
  }
  .card-title strong { font-weight: 600; }
  .title-rule {
    position: absolute;
    left: 97px; top: 59px;
    width: 164px; height: 1px;
    background: linear-gradient(90deg, transparent, #6a6a6a, transparent);
  }
  .field-label {
    position: absolute;
    left: 44px;
    font-size: 11px;
    font-weight: 400;
  }
  .field-input {
    position: absolute;
    left: 45px;
    width: 263px;
    border-radius: 2px;
    background: var(--field);
  }
  .submit-button {
    position: absolute;
    left: 44px; top: 356px;
    width: 264px; height: 35px;
    border-radius: 2px;
    background: linear-gradient(180deg, var(--gold-top), var(--gold-bottom));
    color: #fff;
    font-size: 11px;
    display: flex; align-items: center; justify-content: center;
  }
</style>
</head>
<body>
  <header class="brand">
    <div class="brand-name">MARLOW CREST ADVISORY SERVICES</div>
    <div class="brand-tagline">TRUSTED MEDICAL WITNESS COORDINATION</div>
  </header>

  <section class="liaison-card">
    <h1 class="card-title">Connect with one of our <strong>Liaisons</strong></h1>
    <div class="title-rule"></div>

    <span class="field-label" style="top:71px">Name</span>
    <div class="field-input" style="top:87px;height:34px"></div>

    <span class="field-label" style="top:129px">Email</span>
    <div class="field-input" style="top:145px;height:34px"></div>

    <span class="field-label" style="top:186px">Contact Info</span>
    <div class="field-input" style="top:202px;height:34px"></div>

    <span class="field-label" style="top:244px">Description of Project</span>
    <div class="field-input" style="top:260px;height:85px"></div>

    <div class="submit-button">Connect with a Liaison</div>
  </section>
</body>
</html>
```